The Harlow Law Firm, PC

Dwight K. Harlow
Attorney at Law
physical address: 287 E. 9th Avenue
Cedarton, EX 27019

mailing: P.O. Box 5843
Cedarton, EX 27021

o. 555.416.2071
f. 555.416.8532

www.harlowlegal-ex.com

Industry/Entity Type

Attorney

Contact Information for Business Card

Attorney name
Office Phone number
Office Fax number
Mailing address and physical address
website address

Requirements
Must have
• Clean fresh design - I hate the website

```html
<!DOCTYPE html>
<html lang="en">
<head>
<meta charset="utf-8">
<title>Harlow Law Firm Stationery</title>
<link rel="stylesheet" href="https://fonts.googleapis.com/css2?family=Tinos:wght@400;700&display=swap">
<style>
  :root {
    --gold: #c6aa6b;
    --maroon: #7a2630;
    --ink: #1b1b1b;
    --paper: #ffffff;
    --backdrop: #ffffff;
    --edge: #dcdcdc;
  }
  * { margin: 0; padding: 0; box-sizing: border-box; }
  html, body { width: 1200px; height: 930px; overflow: hidden; background: var(--backdrop); }
  body { position: relative; font-family: "Tinos", "Times New Roman", serif; color: var(--ink); }

  .sheet, .card {
    position: absolute;
    background: var(--paper);
    border: 1px solid var(--edge);
    overflow: hidden;
  }
  .sheet { left: 215px; top: 117px; width: 535px; height: 690px; }
  .card { left: 580px; top: 352px; width: 380px; height: 218px; }

  .band { position: absolute; left: 0; right: 0; background: var(--gold); }

  .brand {
    position: absolute; left: 50%; transform: translateX(-50%);
    display: flex; align-items: center; gap: 6px;
    background: var(--paper); padding: 0 8px;
    color: var(--maroon); font-weight: 400; white-space: nowrap;
  }
  .brand-square { background: var(--maroon); flex: none; }

  .identity { position: absolute; left: 0; right: 0; text-align: center; }
  .attorney-name {
    font-weight: 700; font-variant: small-caps; letter-spacing: 0.5px;
    display: inline-block; border-bottom: 1px solid var(--ink); line-height: 1.05;
  }
  .attorney-title { color: var(--maroon); text-transform: uppercase; letter-spacing: 0.3px; line-height: 1.2; }

  .contact { position: absolute; left: 0; right: 0; text-align: center; line-height: 1.45; white-space: nowrap; }

  /* Letterhead */
  .sheet .band-top { top: 0; height: 28px; }
  .sheet .band-rule { top: 34px; height: 7px; }
  .sheet .band-foot { bottom: 0; height: 16px; }
  .sheet .brand { top: 12px; height: 52px; font-size: 17px; }
  .sheet .brand-square { width: 14px; height: 14px; }
  .sheet .identity { top: 74px; }
  .sheet .attorney-name { font-size: 27px; }
  .sheet .attorney-title { font-size: 16px; }
  .sheet .contact { bottom: 26px; font-size: 8.5px; }

  /* Business card */
  .card .band-top { top: 0; height: 15px; }
  .card .band-rule { top: 22px; height: 8px; }
  .card .band-foot { bottom: 0; height: 10px; }
  .card .brand { top: 8px; height: 34px; font-size: 11px; padding: 0 5px; gap: 4px; }
  .card .brand-square { width: 8px; height: 8px; }
  .card .identity { top: 52px; }
  .card .attorney-name { font-size: 22px; }
  .card .attorney-title { font-size: 13px; }
  .card .contact { top: 118px; font-size: 10.5px; line-height: 1.55; }
</style>
</head>
<body>

  <section class="sheet" aria-label="Letterhead">
    <div class="band band-top"></div>
    <div class="band band-rule"></div>
    <div class="brand"><span class="brand-square"></span>Harlow Law Firm</div>
    <div class="identity">
      <div class="attorney-name">Dwight K. Harlow</div>
      <div class="attorney-title">Attorney at Law</div>
    </div>
    <div class="contact">
      287 E. 9th Avenue • Cedarton, EX 27019 / Mailing: P.O. Box 5843 • Cedarton, EX 27021<br>
      Tele: (555) 416-2071 • Fax: (555) 416-8532<br>
      www.harlowlegal-ex.com
    </div>
    <div class="band band-foot"></div>
  </section>

  <section class="card" aria-label="Business card">
    <div class="band band-top"></div>
    <div class="band band-rule"></div>
    <div class="brand"><span class="brand-square"></span>Harlow Law Firm</div>
    <div class="identity">
      <div class="attorney-name">Dwight K. Harlow</div>
      <div class="attorney-title">Attorney at Law</div>
    </div>
    <div class="contact">
      287 E. 9th Avenue • Cedarton, EX 27019<br>
      Mailing: P.O. Box 5843 • Cedarton, EX 27021<br>
      Tele: (555) 416-2071<br>
      Fax: (555) 416-8532<br>
      www.harlowlegal-ex.com
    </div>
    <div class="band band-foot"></div>
  </section>

</body>
</html>
```